Corporate-Design für Unternehmensberatung
Zielgruppe
Unternehmensberatung aus Tübingen, spezialisiert auf Change Management, Personalentwicklung und Organisationsentwicklung. Zielgruppe sind international agierende Top-Unternehmen.
Aufgabenstellung
Farbschema:
Hex: # 918f8b Pantone: Cool Gray 8 C
Hex: # 921108 Pantone: 7621 C,
vgl. PDF Datei.
Gerne nur Bildmarke ohne Schriftzug, Schriftzug allerdings nicht ohne Bildmarke zu verwenden.

```html
<!DOCTYPE html>
<html lang="de">
<head>
<meta charset="utf-8">
<title>Kehrwerk – Geschäftsausstattung</title>
<link href="https://fonts.googleapis.com/css2?family=Montserrat:wght@300;400;600&display=swap" rel="stylesheet">
<style>
  :root {
    --backdrop: #e5e5e5;
    --paper: #ffffff;
    --card-light: #f7f7f7;
    --ink-dark: #111111;
    --brand-red: #921108;
    --brand-grey: #918f8b;
    --brand-light: #c9c7c3;
    --tint-red: #eedbda;
    --tint-dark: #262222;
    --text-grey: #555555;
    --rule: #9a9a9a;
  }
  * { margin: 0; padding: 0; box-sizing: border-box; }
  html, body { width: 1200px; height: 1200px; overflow: hidden; }
  body {
    background: var(--backdrop);
    font-family: "Montserrat", sans-serif;
    position: relative;
  }
  .piece { position: absolute; overflow: hidden; }

  .brand { display: flex; align-items: center; gap: 7px; }
  .brand-square {
    border: 2px solid var(--brand-red);
    border-radius: 2px;
    flex: none;
  }
  .brand-name {
    color: var(--brand-red);
    font-weight: 300;
    letter-spacing: 0.2px;
    line-height: 1;
  }

  .contact { list-style: none; color: var(--text-grey); font-weight: 400; }
  .contact li { display: flex; align-items: flex-start; gap: 5px; line-height: 1.3; }
  .contact svg { flex: none; margin-top: 1px; fill: var(--brand-red); }

  .watermark-square {
    position: absolute;
    border-style: solid;
    border-color: var(--tint-red);
    border-radius: 18px;
  }

  /* Letterhead */
  .letterhead { left: 64px; top: 268px; width: 471px; height: 663px; background: var(--paper); }
  .letterhead .brand { position: absolute; left: 32px; top: 45px; }
  .letterhead .brand-square { width: 22px; height: 22px; }
  .letterhead .brand-name { font-size: 16px; }
  .letterhead .contact { position: absolute; left: 363px; top: 42px; font-size: 6px; }
  .letterhead .contact svg { width: 6px; height: 6px; }
  .letterhead-rule { position: absolute; left: 32px; top: 91px; width: 405px; height: 1px; background: var(--rule); }
  .letterhead .watermark-square { left: 108px; top: 251px; width: 254px; height: 254px; border-width: 20px; border-radius: 40px; }

  /* Business cards */
  .card { top: 326px; width: 196px; height: 112px; }
  .card-front { left: 632px; background: var(--card-light); }
  .card-front .brand { position: absolute; left: 14px; top: 16px; gap: 5px; }
  .card-front .brand-square { width: 14px; height: 14px; border-width: 1.5px; }
  .card-front .brand-name { font-size: 10.5px; }
  .card-front .watermark-square { left: 156px; top: 18px; width: 80px; height: 80px; border-width: 6px; border-radius: 12px; }
  .card-holder { position: absolute; left: 36px; top: 54px; }
  .holder-name { font-size: 7px; font-weight: 600; color: #333; }
  .holder-role { font-size: 4.5px; letter-spacing: 1.5px; color: var(--text-grey); }
  .card-front .contact { position: absolute; left: 36px; top: 71px; font-size: 4.8px; }
  .card-front .contact svg { width: 5px; height: 5px; }

  .card-back { left: 926px; background: var(--ink-dark); }
  .card-back .watermark-square { left: -30px; top: 16px; width: 70px; height: 70px; border-width: 7px; border-color: var(--tint-dark); border-radius: 12px; }
  .card-back .brand { position: absolute; right: 18px; top: 46px; gap: 6px; }
  .card-back .brand-square { width: 18px; height: 18px; }
  .card-back .brand-name { font-size: 14px; color: var(--brand-light); font-weight: 400; }

  /* Envelope */
  .envelope { left: 612px; top: 533px; width: 531px; height: 329px; background: var(--paper); }
  .envelope-flap { position: absolute; left: 0; top: 0; width: 531px; height: 98px; }
  .envelope-flap polygon { fill: var(--ink-dark); }
  .flap-square {
    position: absolute; left: 257px; top: 40px; width: 18px; height: 18px;
    border: 1.5px solid var(--brand-red); border-radius: 2px;
  }
  .envelope .brand { position: absolute; left: 32px; top: 127px; }
  .envelope .brand-square { width: 22px; height: 22px; }
  .envelope .brand-name { font-size: 16px; }
  .envelope .contact { position: absolute; left: 64px; top: 161px; font-size: 6.3px; }
  .envelope .contact svg { width: 6px; height: 6px; }
</style>
</head>
<body>

<svg width="0" height="0" style="position:absolute" aria-hidden="true">
  <defs>
    <symbol id="icon-pin" viewBox="0 0 10 10"><path d="M5 0a3.5 3.5 0 0 0-3.5 3.5C1.5 6 5 10 5 10s3.5-4 3.5-6.5A3.5 3.5 0 0 0 5 0zm0 5a1.4 1.4 0 1 1 0-2.8A1.4 1.4 0 0 1 5 5z"/></symbol>
    <symbol id="icon-phone" viewBox="0 0 10 10"><path d="M2 0.5l2 2-1 1.3c.6 1.3 1.7 2.4 3 3l1.3-1 2 2L8 9.5C4 9.5 .5 6 .5 2z"/></symbol>
    <symbol id="icon-mail" viewBox="0 0 10 10"><path d="M0 2h10v6H0z"/></symbol>
  </defs>
</svg>

<section class="piece letterhead">
  <div class="brand"><span class="brand-square"></span><span class="brand-name">Kehrwerk</span></div>
  <ul class="contact">
    <li><svg><use href="#icon-pin"/></svg><span>Lindenallee 12<br>D - 72070 Tübingen</span></li>
    <li><svg><use href="#icon-phone"/></svg><span>+49 7071 555010</span></li>
    <li><svg><use href="#icon-mail"/></svg><span>ja@kehrwerk-beratung.de</span></li>
  </ul>
  <div class="letterhead-rule"></div>
  <span class="watermark-square" aria-hidden="true"></span>
</section>

<section class="piece card card-front">
  <span class="watermark-square" aria-hidden="true"></span>
  <div class="brand"><span class="brand-square"></span><span class="brand-name">Kehrwerk</span></div>
  <div class="card-holder">
    <p class="holder-name">Jonas Albrecht</p>
    <p class="holder-role">CEO</p>
  </div>
  <ul class="contact">
    <li><svg><use href="#icon-pin"/></svg><span>Lindenallee 12<br>D - 72070 Tübingen</span></li>
    <li><svg><use href="#icon-phone"/></svg><span>+49 7071 555010</span></li>
    <li><svg><use href="#icon-mail"/></svg><span>ja@kehrwerk-beratung.de</span></li>
  </ul>
</section>

<section class="piece card card-back">
  <span class="watermark-square" aria-hidden="true"></span>
  <div class="brand"><span class="brand-square"></span><span class="brand-name">Kehrwerk</span></div>
</section>

<section class="piece envelope">
  <svg class="envelope-flap" viewBox="0 0 531 98" aria-hidden="true">
    <polygon points="21,0 510,0 531,98 0,98"/>
  </svg>
  <span class="flap-square"></span>
  <div class="brand"><span class="brand-square"></span><span class="brand-name">Kehrwerk</span></div>
  <ul class="contact">
    <li><svg><use href="#icon-pin"/></svg><span>Lindenallee 12<br>D - 72070 Tübingen</span></li>
    <li><svg><use href="#icon-phone"/></svg><span>+49 7071 555010</span></li>
    <li><svg><use href="#icon-mail"/></svg><span>ja@kehrwerk-beratung.de</span></li>
  </ul>
</section>

</body>
</html>
```